web design for specialty coffee shop

We are online shop selling specialty coffeee.
Our brand concept keywords are -
specialty coffee, knowledge, discovery, professional, convenience, collaboration.
there will be five main tabs on the homepage
[home (u icon from logo)]
[coffee]
[equipment]
[gift]
[knowledge]
[about us]
For our site, we will be using the following template.
ONLY DESIGN, NO CODING necessary as our developers will do that.
http://plendrixthemes.net/item/velmora-premium-responsive-shopcart-theme/full_screen_preview/7302514
Use the template as a base.
You do not have to do exactly the same layout.
Creative Liberty!
For the style and color palette, please look at the attached image.
Our brown logo should match nicely with the style provided in the attachment.
Thank you for taking the time to read this post.
Looking forward to working with artquivery and the amazing designers that are part of this community.
Reason: Dear designers,
I have extended the deadline to give designers who accepted to participate in this contest some more time to submit their designs. Thank you for understanding.
Coffee Shop

```html
<!DOCTYPE html>
<html lang="en">
<head>
<meta charset="utf-8">
<title>Kindred Coffee Lab</title>
<link href="https://fonts.googleapis.com/css2?family=Ultra&family=Yanone+Kaffeesatz:wght@400;500&family=Arimo:wght@400;700&family=Fira+Mono&display=swap" rel="stylesheet">
<style>
:root{
  --teal:#4fb3b8;
  --cream:#fbefd2;
  --cream-deep:#f6e3bb;
  --maroon:#2a0000;
  --brown:#7a4312;
  --brown-dark:#3a1508;
  --rust:#8b4f14;
  --white:#ffffff;
  --footer:#000000;
  --footer-text:#a39b90;
}
*{margin:0;padding:0;box-sizing:border-box}
html,body{width:1200px;height:880px;overflow:hidden}
body{position:relative;background:var(--cream);font-family:'Arimo',sans-serif}
.account-bar{position:absolute;left:0;top:0;width:1200px;height:40px;background:var(--teal)}
.account-links{position:absolute;right:240px;top:0;height:40px;display:flex;list-style:none}
.account-links li{font-size:10px;color:var(--white);line-height:40px;padding:0 12px;border-left:1px solid rgba(0,0,0,.12)}
.account-links li:first-child{border-left:none}
.masthead{position:absolute;left:0;top:40px;width:1200px;height:112px;background:linear-gradient(90deg,var(--cream-deep),var(--cream) 20%,var(--cream) 80%,var(--cream-deep))}
.brand{position:absolute;left:0;width:1200px;top:52px;text-align:center;color:var(--brown-dark)}
.brand-mark{display:block;margin:0 auto 6px;width:30px;height:30px;border-radius:50%;background:var(--brown-dark)}
.brand-name{display:block;font-family:'Arimo',sans-serif;font-weight:700;font-size:32px;line-height:30px}
.brand-sub{display:block;font-family:'Fira Mono',monospace;font-size:10px;letter-spacing:3px;margin-top:2px}
.main-nav{position:absolute;left:0;top:152px;width:1200px;height:44px;background:var(--maroon);display:flex;justify-content:center;list-style:none}
.main-nav li{color:var(--white);font-weight:700;font-size:12px;line-height:44px;padding:0 8px}
.hero{position:absolute;left:0;top:196px;width:1200px;height:384px;background:radial-gradient(ellipse at 35% 45%,#e6a578 0%,#c27d48 25%,#9a5a2a 55%,#6e3a18 80%,#8f5223 100%)}
.hero-title{position:absolute;right:234px;top:73px;font-family:'Ultra',serif;font-size:22px;color:var(--white);letter-spacing:1px}
.hero-sub{position:absolute;right:234px;top:104px;font-family:'Yanone Kaffeesatz',sans-serif;font-weight:500;font-size:24px;color:var(--teal)}
.hero-copy{position:absolute;right:234px;top:142px;width:150px;text-align:right;font-family:'Yanone Kaffeesatz',sans-serif;font-size:15px;line-height:14.4px;color:var(--teal);text-transform:uppercase}
.slide-arrow{position:absolute;top:144px}
.slide-arrow.prev{left:15px}
.slide-arrow.next{left:1161px}
.slide-dots{position:absolute;left:892px;top:363px;display:flex;gap:4px}
.slide-dots span{width:8px;height:8px;border-radius:50%;background:var(--white)}
.slide-dots .active{background:var(--teal)}
.steps-title{position:absolute;left:0;width:1200px;top:606px;text-align:center;font-family:'Ultra',serif;font-size:17px;color:var(--rust)}
.steps-title svg{position:absolute;left:694px;top:6px}
.steps{position:absolute;left:0;top:672px;width:1200px;list-style:none}
.step{position:absolute;width:180px;margin-left:-90px;text-align:center}
.step-icon{display:block;margin:0 auto;height:74px}
.step-label{display:block;margin-top:6px;font-family:'Yanone Kaffeesatz',sans-serif;font-size:14px;line-height:13px;color:var(--teal);text-transform:uppercase}
.site-footer{position:absolute;left:0;top:838px;width:1200px;height:42px;background:var(--footer)}
.copyright{position:absolute;left:0;width:1140px;top:0;line-height:48px;text-align:center;font-size:10px;color:var(--footer-text)}
.social-square{position:absolute;left:896px;top:5px;width:31px;height:31px;border-radius:3px;background:#3a3a3a}
</style>
</head>
<body>
<header class="account-bar">
  <ul class="account-links"><li>Sign in</li><li>Register</li><li>Cart (0)</li></ul>
</header>
<div class="masthead"></div>
<div class="brand">
  <span class="brand-mark"></span>
  <span class="brand-name">kindred</span>
  <span class="brand-sub">coffee lab</span>
</div>
<ul class="main-nav"><li>COFFEE</li><li>EQUIPMENT</li><li>GIFT</li><li>KNOWLEDGE</li><li>ABOUT US</li></ul>
<section class="hero" role="img" aria-label="Photo of a woman sipping from a white cup, warm brown tones">
  <svg class="slide-arrow prev" width="28" height="38" viewBox="0 0 28 38"><path d="M26 2 L3 19 L26 36 Z" fill="none" stroke="#b9b3ae" stroke-width="4"/></svg>
  <svg class="slide-arrow next" width="28" height="38" viewBox="0 0 28 38"><path d="M2 2 L25 19 L2 36 Z" fill="none" stroke="#b9b3ae" stroke-width="4"/></svg>
  <h1 class="hero-title">CHOOSE YOUR TASTE !</h1>
  <p class="hero-sub">IN 3 EASY STEPS</p>
  <p class="hero-copy">Lorem ipsum dolor sit amet, consectetuer adipiscing elit. Nam cursus. Morbi ut mi. Nullam enim leo, egestas id, condimentum at, laoreet mattis, massa. Sed eleifend</p>
  <div class="slide-dots"><span></span><span></span><span></span><span class="active"></span><span></span></div>
</section>
<h2 class="steps-title">HOW IT WORKS !
  <svg width="26" height="22" viewBox="0 0 26 22"><path d="M2 4 Q14 -2 20 14" fill="none" stroke="#4fb3b8" stroke-width="3" stroke-linecap="round"/><path d="M14 13 L20 17 L23 10" fill="none" stroke="#4fb3b8" stroke-width="3" stroke-linecap="round"/></svg>
</h2>
<ul class="steps">
  <li class="step" style="left:323px">
    <svg class="step-icon" width="70" height="74" role="img" aria-label="Icon of a coffee mug with a dollar sign"><rect x="18" y="8" width="48" height="56" rx="6" fill="#8a4a15"/></svg>
    <span class="step-label">Choose your<br>subscription</span>
  </li>
  <li class="step" style="left:495px">
    <svg class="step-icon" width="90" height="74" role="img" aria-label="Icon of an open cardboard box"><rect x="10" y="6" width="70" height="64" rx="3" fill="#7a4312"/></svg>
    <span class="step-label">Your kindred<br>box delivered</span>
  </li>
  <li class="step" style="left:667px">
    <svg class="step-icon" width="70" height="74" role="img" aria-label="Icon of three coffee beans"><rect x="6" y="6" width="58" height="64" rx="20" fill="#7a4312"/></svg>
    <span class="step-label">Brew 4 coffees<br>and pick a favourite</span>
  </li>
  <li class="step" style="left:851px">
    <svg class="step-icon" width="70" height="80" role="img" aria-label="Shopping bag"><path d="M24 18 V12 a11 11 0 0 1 22 0 V18" fill="none" stroke="#6a3a12" stroke-width="4"/><rect x="5" y="18" width="60" height="58" rx="6" fill="#6a3a12"/></svg>
    <span class="step-label">Get a full bag<br>with free shipping</span>
  </li>
</ul>
<footer class="site-footer">
  <p class="copyright">© copyright Kindred Coffee Lab 2013. All rights reserved</p>
  <span class="social-square"></span>
</footer>
</body>
</html>
```